Flyer design for the Harvest Lantern Summit 2019 (HALSUM)

Design a flyer for our annual conference with basic information about the conference: conference logo and year, Conference name: Harvest Lantern Summit Location: Talbot Community Center (Downtown Portland)482 Wexley Street, Portland, ME 04109, Date: August 8th, 9th, 10th and 11th, 2019Start time 7:00PMI would like the following three words added to the flyer. These words describe the vision of the conference: Prophetic, Fire, Overflow,

Contact info:
Website: www.vostel.org
Phone: 207 555 3184
Email: contact@meadowcrest.org

Target Market(s)

Young adults living in the United States

Industry/Entity Type

Religious

Font styles to use
Sans Serif

Colors

Designer to choose colors to be used in the design.

Requirements
Must have
• HALSUM must logo standout, the reader should be able to take a quick look and find key info,
Should not have
• Cross image, church image

```html
<!DOCTYPE html>
<html lang="en">
<head>
<meta charset="utf-8">
<title>Harvest Lantern Summit 2019</title>
<link rel="stylesheet" href="https://fonts.googleapis.com/css2?family=Josefin+Sans:wght@400;600;700&family=Nunito:wght@800&family=Montserrat:wght@700&family=Arimo&display=swap">
<style>
  :root {
    --sky-light: #5fd6fa;
    --sky-mid: #36a6f3;
    --sky-deep: #1553ee;
    --cloud: #eefcf9;
    --cloud-warm: #fbf9dc;
    --illustration-top: #dfe9f0;
    --illustration-bottom: #f1b89a;
    --brand-blue: #2f86e8;
    --brand-orange: #f7891f;
    --white: #ffffff;
  }
  * { margin: 0; padding: 0; box-sizing: border-box; }
  html, body { width: 850px; height: 1200px; overflow: hidden; }
  body { background: var(--white); }
  .flyer {
    position: relative;
    width: 850px;
    height: 1200px;
    overflow: hidden;
    background:
      radial-gradient(circle at 235px 330px, rgba(255,255,255,0.35), rgba(255,255,255,0) 420px),
      linear-gradient(100deg, var(--sky-light) 0%, var(--sky-mid) 50%, var(--sky-deep) 100%);
    font-family: "Josefin Sans", sans-serif;
    color: var(--white);
  }
  .clouds {
    position: absolute;
    left: 0; top: 660px;
    width: 850px; height: 480px;
    background:
      radial-gradient(ellipse 260px 150px at 430px 300px, var(--cloud-warm), rgba(251,249,220,0) 100%),
      linear-gradient(180deg, rgba(238,252,249,0) 0%, rgba(238,252,249,0.85) 28%, var(--cloud) 55%);
  }
  .illustration {
    position: absolute;
    left: 135px; top: 262px;
    width: 200px; height: 610px;
    background: linear-gradient(180deg, var(--illustration-top) 0%, var(--illustration-bottom) 100%);
    opacity: 0.55;
  }
  .title {
    position: absolute;
    left: 68px; top: 63px;
    font-weight: 600;
    font-size: 51px;
    line-height: 59px;
    text-transform: uppercase;
  }
  .vision {
    position: absolute;
    left: 508px; top: 50px;
    list-style: none;
  }
  .vision li {
    display: flex;
    align-items: center;
    height: 62px;
    font-family: "Nunito", sans-serif;
    font-weight: 800;
    font-size: 37px;
    color: var(--brand-orange);
  }
  .vision li:nth-child(3) { margin-top: 4px; }
  .vision .dot {
    width: 30px; height: 30px;
    border-radius: 50%;
    background: var(--brand-orange);
    margin-right: 16px;
  }
  .details { position: absolute; left: 517px; top: 356px; width: 320px; }
  .details .icon { display: block; }
  .date {
    margin-top: 12px;
    font-weight: 700;
    font-size: 26px;
    line-height: 31px;
  }
  .pin { margin-top: 30px; }
  .venue {
    margin-top: 16px;
    font-size: 21px;
    line-height: 25.5px;
  }
  .venue .venue-name { font-weight: 700; }
  .clock { margin-top: 30px; }
  .start {
    margin-top: 22px;
    font-size: 21px;
  }
  .start strong { font-weight: 700; }
  .logo {
    position: absolute;
    left: 0; top: 908px;
    width: 850px;
    text-align: center;
  }
  .logo-name {
    font-family: "Montserrat", sans-serif;
    font-weight: 700;
    font-size: 138px;
    line-height: 136px;
    color: var(--brand-blue);
    letter-spacing: 3px;
  }
  .logo-year {
    margin-top: 4px;
    display: flex;
    align-items: center;
    justify-content: center;
    gap: 16px;
    font-family: "Montserrat", sans-serif;
    font-weight: 700;
    font-size: 60px;
    line-height: 64px;
    color: var(--brand-orange);
    letter-spacing: 40px;
  }
  .logo-year .rule { width: 165px; height: 4px; background: var(--brand-orange); }
  .logo-year .year { padding-left: 40px; margin-right: -22px; }
  .contact-bar {
    position: absolute;
    left: 0; top: 1131px;
    width: 850px; height: 69px;
    background: var(--brand-orange);
    display: flex;
    align-items: center;
    justify-content: center;
    gap: 30px;
    font-family: "Arimo", sans-serif;
    font-size: 19.5px;
  }
  .contact-bar .item { display: flex; align-items: center; gap: 10px; }
  .contact-bar svg { display: block; }
</style>
</head>
<body>
<main class="flyer">
  <div class="clouds" role="img" aria-label="Soft white clouds at the base of the sky"></div>
  <div class="illustration" role="img" aria-label="Illustration area: a rocket lifting off with flaming boosters"></div>

  <h1 class="title">Harvest<br>Lantern<br>Summit</h1>

  <ul class="vision">
    <li><span class="dot"></span>Prophetic</li>
    <li><span class="dot"></span>Fire</li>
    <li><span class="dot"></span>Overflow</li>
  </ul>

  <section class="details">
    <svg class="icon calendar" width="37" height="36" viewBox="0 0 37 36" fill="none" stroke="#fff" stroke-width="2.5">
      <rect x="1.5" y="4" width="34" height="30" rx="2"/>
      <line x1="9" y1="1" x2="9" y2="7"/><line x1="28" y1="1" x2="28" y2="7"/>
      <line x1="1.5" y1="12" x2="35.5" y2="12"/>
      <g fill="#fff" stroke="none">
        <rect x="7" y="16" width="4" height="3"/><rect x="13" y="16" width="4" height="3"/><rect x="19" y="16" width="4" height="3"/><rect x="25" y="16" width="4" height="3"/>
        <rect x="7" y="22" width="4" height="3"/><rect x="13" y="22" width="4" height="3"/><rect x="19" y="22" width="4" height="3"/><rect x="25" y="22" width="4" height="3"/>
        <rect x="7" y="28" width="4" height="3"/><rect x="13" y="28" width="4" height="3"/><rect x="19" y="28" width="4" height="3"/>
      </g>
    </svg>
    <p class="date">August 8th, 9th,<br>10th and 11th, 2019</p>

    <svg class="icon pin" width="30" height="40" viewBox="0 0 30 40">
      <path d="M15 0C6.7 0 0 6.7 0 15c0 10.5 15 25 15 25s15-14.5 15-25C30 6.7 23.3 0 15 0z" fill="#fff"/>
      <circle cx="15" cy="14" r="5.5" fill="#2f86e8"/>
    </svg>
    <p class="venue">
      <span class="venue-name">Talbot Community Center</span><br>
      (Downtown Portland)<br>
      482 Wexley Street,<br>
      Portland, ME 04109
    </p>

    <svg class="icon clock" width="38" height="38" viewBox="0 0 38 38" fill="none" stroke="#fff" stroke-width="4">
      <circle cx="19" cy="19" r="16.5"/>
      <polyline points="19,9 19,20 27,20" stroke-width="3.5"/>
    </svg>
    <p class="start">Start time <strong>7:00 PM</strong></p>
  </section>

  <div class="logo">
    <div class="logo-name">HALSUM</div>
    <div class="logo-year"><span class="rule"></span><span class="year">2019</span><span class="rule"></span></div>
  </div>

  <footer class="contact-bar">
    <span class="item">
      <svg width="20" height="30" viewBox="0 0 20 30"><path d="M6 1c-3 1-5 3-5 7 0 7 4 16 10 20 2 1 4 1 6-1l1-2-5-5-2 1c-2-2-4-7-4-10l2-1-1-7z" fill="#2f86e8"/></svg>
      207 555 3184
    </span>
    <span class="item">
      <svg width="32" height="22" viewBox="0 0 32 22" fill="none" stroke="#2f86e8" stroke-width="2"><rect x="1" y="1" width="30" height="20"/><polyline points="1,1 16,13 31,1"/><line x1="1" y1="21" x2="12" y2="10"/><line x1="31" y1="21" x2="20" y2="10"/></svg>
      contact@meadowcrest.org
    </span>
    <span class="item">
      <svg width="26" height="26" viewBox="0 0 26 26" fill="none" stroke="#2f86e8" stroke-width="1.8"><circle cx="13" cy="13" r="11.5"/><ellipse cx="13" cy="13" rx="5" ry="11.5"/><line x1="1.5" y1="13" x2="24.5" y2="13"/><line x1="3.5" y1="7" x2="22.5" y2="7"/><line x1="3.5" y1="19" x2="22.5" y2="19"/></svg>
      www.vostel.org
    </span>
  </footer>
</main>
</body>
</html>
```